Tri-fold Brochure Design for Banking Business

The brochure we have needs to be improved - more business like and more attractive. Logo file and brochure is attached. I would like to be able to edit the text after you get done. Your ideas and changes to text are welcome. See our website www.korvanbridgegrp.com for our theme. We can use indesign to edit the text after you complete. However, please make changes to the text we have in the design that it uploaded. Your comments and changes are welcome.

Target Market(s)

Human Resources and learning & development staff at the global investment banks - Pellham Trask, QWNR, etc.

Industry/Entity Type

Investment Banking

Logo Text

Korvan Bridge Group

Font styles to use
Serif
Sans Serif

Colors
33a6d7
0493ce
3277b5
fbf289
fdf9cf
fbee3e
0555a3
85acd3

Requirements
Must have
• Must be similar to our website www.korvanbridgegrp.com. Needs to be business-like, clean fonts, sharp design. Our logo - of course.
Nice to have
• City images - seems to be our theme.

```html
<!DOCTYPE html>
<html lang="en">
<head>
<meta charset="utf-8">
<title>Korvan Bridge Group – Brochure Inside Panel</title>
<link href="https://fonts.googleapis.com/css2?family=Lexend+Exa:wght@500&family=Montserrat:wght@300;400;600&display=swap" rel="stylesheet">
<style>
  :root {
    --band-blue: #3a8cf2;
    --accent-blue: #2f86ef;
    --heading-yellow: #f3ea3c;
    --text-dark: #1d1d1f;
    --page-bg: #ffffff;
    --sheet-bg: #fdfdfd;
    --city-sky: #bcd3ec;
    --city-deep: #3d6fa8;
    --training-light: #a9cdf0;
    --training-deep: #2b5f9e;
    --team-sky: #dbe8f5;
    --team-deep: #4d7fae;
  }
  * { box-sizing: border-box; margin: 0; padding: 0; }
  html, body { width: 1200px; height: 1000px; overflow: hidden; background: var(--page-bg); }
  body { position: relative; font-family: "Montserrat", Arial, sans-serif; color: var(--text-dark); }

  .sheet { position: absolute; left: 28px; top: 57px; width: 1144px; height: 886px; background: var(--sheet-bg); }

  .section-band {
    position: absolute; left: 28px; width: 385px;
    background: var(--band-blue);
    display: flex; align-items: center; justify-content: center;
  }
  .section-title {
    font-family: "Lexend Exa", "Montserrat", sans-serif;
    font-weight: 500; font-size: 27px; letter-spacing: 0.5px;
    color: var(--heading-yellow); text-transform: uppercase;
  }
  .section-photo { position: absolute; left: 28px; width: 385px; }
  .photo-city { top: 182px; height: 166px; background: linear-gradient(180deg, var(--city-sky) 0%, #8fb2da 55%, var(--city-deep) 100%); }
  .photo-training { top: 476px; height: 171px; background: radial-gradient(circle at 40% 45%, var(--training-light) 0%, #5f97d4 55%, var(--training-deep) 100%); }
  .photo-team { top: 772px; height: 171px; background: linear-gradient(180deg, var(--team-sky) 0%, #a8c4e2 55%, var(--team-deep) 100%); }

  .copy { position: absolute; font-size: 15.5px; line-height: 22px; font-weight: 400; }
  .copy p { margin-bottom: 20px; }
  .copy strong { font-weight: 600; }

  .benefit-list { list-style: none; }
  .benefit-list li { position: relative; padding-left: 17px; margin-bottom: 20px; }
  .benefit-list li svg { position: absolute; left: 0; top: 5px; }

  .divider { position: absolute; left: 504px; width: 578px; height: 1.5px; background: var(--accent-blue); }

  .contact-callout { position: absolute; left: 820px; top: 733px; color: var(--accent-blue); }
  .contact-callout h2 { font-weight: 400; font-size: 44px; line-height: 46px; }
  .contact-callout p { font-weight: 400; font-size: 26px; margin-top: 16px; }
</style>
</head>
<body>
  <div class="sheet"></div>

  <!-- Why choose us -->
  <div class="section-band" style="top:57px;height:125px;"><h1 class="section-title">Why choose us?</h1></div>
  <div class="section-photo photo-city" role="img" aria-label="Photo of a harbour city skyline with tall towers under a blue sky"></div>

  <ul class="copy benefit-list" style="left:453px;top:103px;width:330px;">
    <li><svg width="12" height="12" viewBox="0 0 12 12"><path d="M1 0 L11 6 L1 12 Z" fill="var(--accent-blue)"/></svg><strong>Korvan Bridge Group</strong><br>is dedicated to providing you and your firm with the highest level of service.</li>
    <li><svg width="12" height="12" viewBox="0 0 12 12"><path d="M1 0 L11 6 L1 12 Z" fill="var(--accent-blue)"/></svg>We provide dedicated sales and logistics support for each program to insure consistent, reliable results.</li>
  </ul>
  <ul class="copy benefit-list" style="left:819px;top:103px;width:300px;">
    <li><svg width="12" height="12" viewBox="0 0 12 12"><path d="M1 0 L11 6 L1 12 Z" fill="var(--accent-blue)"/></svg>Highly qualified, international pool of trainers</li>
    <li style="margin-bottom:26px;"><svg width="12" height="12" viewBox="0 0 12 12"><path d="M1 0 L11 6 L1 12 Z" fill="var(--accent-blue)"/></svg>Strong client relationship management and support</li>
    <li style="margin-bottom:13px;"><svg width="12" height="12" viewBox="0 0 12 12"><path d="M1 0 L11 6 L1 12 Z" fill="var(--accent-blue)"/></svg>Competitive pricing and flexibility</li>
    <li><svg width="12" height="12" viewBox="0 0 12 12"><path d="M1 0 L11 6 L1 12 Z" fill="var(--accent-blue)"/></svg>Outcome driven approach directly matches your company’s needs</li>
  </ul>

  <div class="divider" style="top:350px;"></div>

  <!-- Our services -->
  <div class="section-band" style="top:348px;height:128px;"><h1 class="section-title">Our services</h1></div>
  <div class="section-photo photo-training" role="img" aria-label="Photo of a businessman touching a digital training interface with skill icons"></div>

  <div class="copy" style="left:439px;top:373px;width:330px;">
    <p style="margin-bottom:29px;"><strong>Korvan Bridge Group</strong> provides best in class services for all our clients.</p>
    <p style="margin-bottom:29px;">We provide highly customized programs tailored to your specific requirements.</p>
    <p>Direct interaction between our clients, consulting trainers and client service staff ensures measurable outcomes for program participants.</p>
  </div>
  <div class="copy" style="left:818px;top:373px;width:330px;">
    <p style="margin-bottom:25px;">We facilitate learning outcomes using a blended methodology combining interactive analysis, hands-on experential models, market simulations and a state-of-the-art learning management system.</p>
    <p>Our material databanks are continuously updated to insure accuracy and effectiveness of our services.</p>
  </div>

  <div class="divider" style="top:645px;"></div>

  <!-- Our team -->
  <div class="section-band" style="top:647px;height:125px;"><h1 class="section-title">Our team</h1></div>
  <div class="section-photo photo-team" role="img" aria-label="Photo of a group of business professionals standing on a globe with city buildings"></div>

  <div class="copy" style="left:439px;top:696px;width:300px;">
    <p style="margin-bottom:27px;">Our <strong>Consulting Trainers</strong> are located globally and recognized by the industry as highly effective trainers and program facilitators.</p>
    <p><strong>Korvan Bridge Group</strong> provides global expertise for our programs with local talent for program facilitation.</p>
  </div>

  <div class="contact-callout">
    <h2>Need more<br>information?</h2>
    <p>Contact us!</p>
  </div>
</body>
</html>
```